New Business Card Design Project

Use the flyer uploaded and website www.brightoakbuilders.com for inspiration.
List Our Services on Backside of business cards
Martin Hollis
Harborline Renovations Inc.
Licensed General Contractors
858-471-9063

Contact Information for Business Card

Use the flyer uploaded and website www.brightoakbuilders.com for inspiration. List Our Services on Backside of business cards Martin Hollis Harborline Renovations Inc. Licensed General Contractors 858-471-9063

```html
<!DOCTYPE html>
<html lang="en">
<head>
<meta charset="utf-8">
<title>Harborline Renovations – Business Card</title>
<link href="https://fonts.googleapis.com/css2?family=Marcellus&family=PT+Sans:wght@400;700&display=swap" rel="stylesheet">
<style>
  :root {
    --backdrop: #2f2f31;
    --card: #141414;
    --ink: #ffffff;
    --ink-dark: #141414;
  }
  html, body {
    margin: 0;
    padding: 0;
    width: 900px;
    height: 1200px;
    overflow: hidden;
    background: var(--backdrop);
  }
  .canvas {
    position: relative;
    width: 900px;
    height: 1200px;
  }
  .card {
    position: absolute;
    left: 134px;
    width: 632px;
    height: 364px;
    background: var(--card);
    color: var(--ink);
    font-family: "PT Sans", sans-serif;
  }
  .card--services { top: 210px; }
  .card--contact { top: 624px; }

  .brand {
    position: absolute;
    left: 30px;
    width: 320px;
    top: 170px;
    display: flex;
    flex-direction: column;
    align-items: center;
    gap: 14px;
  }
  .brand__mark {
    width: 14px;
    height: 14px;
    border: 1.5px solid var(--ink);
  }
  .brand__name {
    font-family: "Marcellus", serif;
    font-size: 22px;
    letter-spacing: 1px;
    white-space: nowrap;
  }

  .services {
    position: absolute;
    left: 372px;
    top: 54px;
  }
  .services__guarantee {
    margin: 0;
    font-weight: 700;
    font-size: 14px;
    line-height: 18px;
    letter-spacing: 0.2px;
  }
  .services__band {
    margin-top: 4px;
    width: 162px;
    height: 18px;
    background: var(--ink);
    clip-path: polygon(0 0, 100% 0, 93% 100%, 0 100%);
    color: var(--ink-dark);
    font-weight: 700;
    font-size: 13px;
    line-height: 18px;
    letter-spacing: 1px;
    padding-left: 21px;
    box-sizing: border-box;
  }
  .services__list {
    list-style: none;
    margin: 5px 0 0;
    padding: 0;
  }
  .services__item {
    display: flex;
    align-items: center;
    gap: 8px;
    font-size: 13.5px;
    line-height: 22.4px;
    letter-spacing: 0.3px;
  }
  .tick { width: 14px; height: 14px; flex: none; }

  .person {
    position: absolute;
    left: 372px;
    top: 88px;
  }
  .person__name {
    margin: 0;
    font-family: "Marcellus", serif;
    font-weight: 400;
    font-size: 26px;
    letter-spacing: 2px;
    line-height: 30px;
  }
  .person__role {
    margin: 4px 0 0;
    font-size: 14px;
    letter-spacing: 0.3px;
  }
  .contact {
    list-style: none;
    margin: 0;
    padding: 0;
    position: absolute;
    left: 372px;
    top: 198px;
  }
  .contact__item {
    display: flex;
    align-items: center;
    gap: 8px;
    font-size: 14px;
    line-height: 25px;
    letter-spacing: 0.6px;
  }
  .contact__icon { width: 14px; height: 14px; flex: none; }
</style>
</head>
<body>
<main class="canvas">

  <section class="card card--services">
    <div class="brand">
      <span class="brand__mark"></span>
      <span class="brand__name">HARBORLINE RENOVATIONS</span>
    </div>

    <div class="services">
      <p class="services__guarantee">OUR SERVICES ARE<br>100% GUARANTEED</p>
      <div class="services__band">SPECIALIZING IN:</div>
      <ul class="services__list">
        <li class="services__item"><svg class="tick" viewBox="0 0 14 14"><rect x="1" y="3" width="10" height="10" fill="none" stroke="#fff" stroke-width="1.6"/><path d="M3.5 7.5 L6 10 L13 1.5" fill="none" stroke="#fff" stroke-width="2"/></svg>Remodel: Kitchen &amp; Bath</li>
        <li class="services__item"><svg class="tick" viewBox="0 0 14 14"><rect x="1" y="3" width="10" height="10" fill="none" stroke="#fff" stroke-width="1.6"/><path d="M3.5 7.5 L6 10 L13 1.5" fill="none" stroke="#fff" stroke-width="2"/></svg>Painting: Interior &amp; Exterior</li>
        <li class="services__item"><svg class="tick" viewBox="0 0 14 14"><rect x="1" y="3" width="10" height="10" fill="none" stroke="#fff" stroke-width="1.6"/><path d="M3.5 7.5 L6 10 L13 1.5" fill="none" stroke="#fff" stroke-width="2"/></svg>Flooring: Carpet, Vinyl, Wood</li>
        <li class="services__item"><svg class="tick" viewBox="0 0 14 14"><rect x="1" y="3" width="10" height="10" fill="none" stroke="#fff" stroke-width="1.6"/><path d="M3.5 7.5 L6 10 L13 1.5" fill="none" stroke="#fff" stroke-width="2"/></svg>Window &amp; Door Replacement</li>
        <li class="services__item"><svg class="tick" viewBox="0 0 14 14"><rect x="1" y="3" width="10" height="10" fill="none" stroke="#fff" stroke-width="1.6"/><path d="M3.5 7.5 L6 10 L13 1.5" fill="none" stroke="#fff" stroke-width="2"/></svg>Plumbing: Repairs &amp; Upgrades</li>
        <li class="services__item"><svg class="tick" viewBox="0 0 14 14"><rect x="1" y="3" width="10" height="10" fill="none" stroke="#fff" stroke-width="1.6"/><path d="M3.5 7.5 L6 10 L13 1.5" fill="none" stroke="#fff" stroke-width="2"/></svg>Energy-Efficient Upgrades</li>
        <li class="services__item"><svg class="tick" viewBox="0 0 14 14"><rect x="1" y="3" width="10" height="10" fill="none" stroke="#fff" stroke-width="1.6"/><path d="M3.5 7.5 L6 10 L13 1.5" fill="none" stroke="#fff" stroke-width="2"/></svg>Deck &amp; Patio Construction</li>
        <li class="services__item"><svg class="tick" viewBox="0 0 14 14"><rect x="1" y="3" width="10" height="10" fill="none" stroke="#fff" stroke-width="1.6"/><path d="M3.5 7.5 L6 10 L13 1.5" fill="none" stroke="#fff" stroke-width="2"/></svg>Water &amp; Mold Damage</li>
        <li class="services__item"><svg class="tick" viewBox="0 0 14 14"><rect x="1" y="3" width="10" height="10" fill="none" stroke="#fff" stroke-width="1.6"/><path d="M3.5 7.5 L6 10 L13 1.5" fill="none" stroke="#fff" stroke-width="2"/></svg>Garage Renovation</li>
      </ul>
    </div>
  </section>

  <section class="card card--contact">
    <div class="brand">
      <span class="brand__mark"></span>
      <span class="brand__name">HARBORLINE RENOVATIONS</span>
    </div>

    <div class="person">
      <h1 class="person__name">MARTIN HOLLIS</h1>
      <p class="person__role">Business development manager</p>
    </div>

    <ul class="contact">
      <li class="contact__item">
        <svg class="contact__icon" viewBox="0 0 16 16"><path d="M3.5 1 L6 1 L7 5 L5.3 6.3 C6.3 8.4 7.6 9.7 9.7 10.7 L11 9 L15 10 L15 12.5 C15 14 14 15 12.5 15 C6.5 15 1 9.5 1 3.5 C1 2 2 1 3.5 1 Z" fill="#fff"/></svg>
        858-471-9063
      </li>
      <li class="contact__item">
        <svg class="contact__icon" viewBox="0 0 16 16"><rect x="1" y="3" width="14" height="10" fill="#fff"/><path d="M1 3 L8 9 L15 3" fill="none" stroke="#141414" stroke-width="1.4"/></svg>
        mh@brightoakbuilders.com
      </li>
      <li class="contact__item">
        <svg class="contact__icon" viewBox="0 0 16 16" fill="none" stroke="#fff" stroke-width="1.3"><circle cx="8" cy="8" r="6.5"/><ellipse cx="8" cy="8" rx="2.8" ry="6.5"/><path d="M1.5 8 H14.5 M2.5 4.8 H13.5 M2.5 11.2 H13.5"/></svg>
        www.brightoakbuilders.com
      </li>
    </ul>
  </section>

</main>
</body>
</html>
```